Course Graduation Certificate

This project is not for a flyer but instead for the creation of a course graduation certificate. The final certificate needs to include the Marlowe Summit Aviation Academy logo and the text stating as follows:
Certifies that ___________________________ has satisfactorily completed the course of _______________________________ on ________________________________
I would also like to include some type of gold seal of completion as well as a place to sign my name and credentials at the bottom of the certificate
I have included the Marlowe Summit Aviation Academy logo as well as three other certificate examples for you to work from.
Target Market(s)
Students completing a certification course and receiving a certificate
Look and feel

```html
<!DOCTYPE html>
<html lang="en">
<head>
<meta charset="utf-8">
<title>Certificate of Graduation – Marlowe Summit Aviation Academy</title>
<link href="https://fonts.googleapis.com/css2?family=Montserrat:ital,wght@0,400;0,600;0,700;1,400;1,700&family=Mrs+Saint+Delafield&display=swap" rel="stylesheet">
<style>
  :root {
    --page-bg: #a9a9a9;
    --frame-dark: #1f2123;
    --gold: #c9a43a;
    --gold-light: #f3d77a;
    --gold-deep: #9c7420;
    --brand-blue: #0a5fb4;
    --paper: #ffffff;
    --ink: #1a1a1a;
    --rule: #555555;
  }
  * { margin: 0; padding: 0; box-sizing: border-box; }
  html, body { width: 800px; height: 1200px; overflow: hidden; }
  body { background: var(--page-bg); font-family: "Montserrat", sans-serif; color: var(--ink); position: relative; }

  .certificate {
    position: absolute; left: 30px; top: 314px;
    width: 740px; height: 572px;
    box-shadow: 0 6px 14px rgba(0,0,0,.35);
  }
  .certificate__frame { position: absolute; inset: 0; }

  .certificate__title {
    position: absolute; left: 86px; top: 66px;
    color: var(--paper); font-weight: 700; font-size: 44px; letter-spacing: 1px; line-height: 1;
  }
  .certificate__subtitle {
    position: absolute; left: 87px; top: 114px;
    color: var(--paper); font-weight: 400; font-size: 22px; letter-spacing: .5px; line-height: 1;
  }
  .academy-name {
    position: absolute; left: 456px; top: 80px; width: 220px;
    display: flex; align-items: center; gap: 10px;
    color: var(--paper); font-weight: 700; font-size: 15px; line-height: 1.25; letter-spacing: 1px;
  }
  .academy-name__mark { width: 14px; height: 14px; border-radius: 50%; background: var(--paper); flex: none; }

  .certifies { position: absolute; left: 0; width: 740px; top: 174px; line-height: 1; text-align: center; font-weight: 700; font-style: italic; font-size: 17px; }
  .recipient { position: absolute; left: 0; width: 740px; top: 214px; text-align: center; font-family: "Mrs Saint Delafield", cursive; font-size: 50px; line-height: 1; }
  .completed { position: absolute; left: 0; width: 740px; top: 274px; line-height: 1; text-align: center; font-style: italic; font-size: 15px; }

  .fill-line { position: absolute; height: 0; border-top: 1px solid var(--rule); }
  .fill-line--course { left: 87px; width: 549px; top: 331px; }
  .fill-line--date { left: 224px; width: 292px; top: 385px; }
  .fill-line--signature { left: 434px; width: 199px; top: 472px; }
  .on-label { position: absolute; left: 189px; top: 373px; line-height: 1; font-style: italic; font-size: 14px; }

  .signatory { position: absolute; left: 433px; top: 482px; font-size: 13px; line-height: 1.45; }
  .signatory__role { font-weight: 400; }
  .signatory__office { font-weight: 700; }

  .completion-seal { position: absolute; left: 111px; top: 400px; width: 116px; height: 116px; }
</style>
</head>
<body>
<main class="certificate">
  <svg class="certificate__frame" viewBox="0 0 740 572" width="740" height="572">
    <defs>
      <linearGradient id="frameShade" x1="0" y1="0" x2="1" y2="1">
        <stop offset="0" stop-color="#2e3336"/><stop offset=".5" stop-color="#1d1f21"/><stop offset="1" stop-color="#2b3034"/>
      </linearGradient>
      <linearGradient id="headerShade" x1="0" y1="0" x2="1" y2="0">
        <stop offset="0" stop-color="#0b6cc8"/><stop offset=".35" stop-color="#0a5fb4"/><stop offset="1" stop-color="#0b5cae"/>
      </linearGradient>
    </defs>
    <rect class="frame-dark" width="740" height="572" fill="url(#frameShade)"/>
    <g class="frame-accents" stroke="var(--gold)" stroke-width="1.4" fill="none">
      <line x1="120" y1="0" x2="0" y2="140"/>
      <line x1="225" y1="0" x2="170" y2="30"/>
      <line x1="0" y1="250" x2="40" y2="190"/>
      <line x1="740" y1="340" x2="690" y2="430"/>
      <line x1="740" y1="400" x2="700" y2="460"/>
      <line x1="480" y1="572" x2="560" y2="530"/>
      <line x1="600" y1="572" x2="640" y2="540"/>
    </g>
    <rect class="paper" x="27" y="27" width="685" height="518" fill="var(--paper)"/>
    <rect class="inner-border" x="36.5" y="36.5" width="667" height="498" fill="none" stroke="var(--brand-blue)" stroke-width="1.5"/>
    <rect class="header-band" x="36" y="36" width="668" height="129" fill="url(#headerShade)"/>
  </svg>

  <h1 class="certificate__title">CERTIFICATE</h1>
  <p class="certificate__subtitle">OF GRADUATION</p>

  <div class="academy-name">
    <span class="academy-name__mark"></span>
    <span>MARLOWE SUMMIT<br>AVIATION ACADEMY</span>
  </div>

  <p class="certifies">Certifies that</p>
  <p class="recipient">Dana Whitlock</p>
  <p class="completed">has satisfactorily completed the course of</p>
  <span class="fill-line fill-line--course"></span>

  <span class="on-label">on</span>
  <span class="fill-line fill-line--date"></span>

  <svg class="completion-seal" viewBox="0 0 116 116" role="img" aria-label="Gold seal of completion">
    <defs>
      <radialGradient id="sealGold" cx=".4" cy=".35" r=".7">
        <stop offset="0" stop-color="var(--gold-light)"/><stop offset=".6" stop-color="var(--gold)"/><stop offset="1" stop-color="var(--gold-deep)"/>
      </radialGradient>
    </defs>
    <circle cx="58" cy="58" r="57" fill="url(#sealGold)"/>
  </svg>

  <span class="fill-line fill-line--signature"></span>
  <div class="signatory">
    <p class="signatory__role">Authorized signatory</p>
    <p class="signatory__office">Harbor Ridge / Eastfield ctr</p>
  </div>
</main>
</body>
</html>
```